Lawn Sign Design – Brisko

We need a clean, eye-catching 18" x 24" lawn sign for Brisko that effectively communicates our core message while maintaining strong brand consistency.

Key Elements to Include:
Tagline (Main Focus): Upgrade Your Roof Without Replacing It
Website: www.tryvexlo-demo.example
Phone Number: (877) BRISKO-GO
RQMH License Number: 4830516
Brisko Logo & Branding: Ensure the logo, corporate colors, and custom font are used consistently to align with our existing branding.

Design Guidelines:
Simple & High-Impact: The tagline should be the most prominent element on the sign, drawing immediate attention.
Easy Readability: Use a bold, clean design with high contrast for quick readability from a distance.
Balanced Layout: Place supporting details (website, phone number, and RQMH number) in a visually clear but secondary position to the tagline.
Professional & Modern: The sign should reflect credibility and innovation in the roofing industry.

Deliverables:
High-resolution print-ready files (CMYK)
A digital proof for review before finalizing
The final design should make a strong impression with minimal text, ensuring that anyone passing by can instantly grasp what we offer.

I am including our custom font. To get an hexagon in our name, simply type the $ after the 'O" Please use this font for anything you type.

```html
<!DOCTYPE html>
<html lang="en">
<head>
<meta charset="utf-8">
<title>Brisko Lawn Sign</title>
<link rel="stylesheet" href="https://fonts.googleapis.com/css2?family=Graduate&family=Oswald:wght@500;600&display=swap">
<style>
  :root {
    --brand-navy: #135197;
    --brand-sky: #2ea8e0;
    --ink: #333333;
    --paper: #ffffff;
  }
  html, body {
    margin: 0;
    padding: 0;
    width: 1200px;
    height: 900px;
    overflow: hidden;
    background: var(--paper);
  }
  .lawn-sign {
    display: block;
    width: 1200px;
    height: 900px;
  }
  .band { fill: var(--brand-navy); }
  .roof-gable { fill: var(--paper); }
  .roof-line { fill: var(--brand-navy); }
  .side-bar { fill: var(--brand-navy); }
  .brand-name {
    font-family: "Graduate", sans-serif;
    fill: var(--brand-navy);
    font-size: 110px;
  }
  .tagline {
    font-family: "Graduate", sans-serif;
    fill: var(--brand-sky);
    font-size: 205px;
  }
  .phone-number {
    font-family: "Graduate", sans-serif;
    fill: var(--brand-navy);
    font-size: 195px;
  }
  .phone-icon-ring { fill: none; stroke: var(--brand-navy); stroke-width: 14; }
  .phone-icon-body { fill: none; stroke: var(--brand-navy); stroke-width: 12; }
  .phone-icon-detail { fill: var(--brand-navy); }
  .license {
    font-family: "Oswald", sans-serif;
    font-weight: 600;
    fill: var(--ink);
    font-size: 88px;
  }
  .website {
    font-family: "Oswald", sans-serif;
    font-weight: 500;
    fill: var(--paper);
    font-size: 122px;
  }
</style>
</head>
<body>
<svg class="lawn-sign" viewBox="0 0 1728 1296" preserveAspectRatio="none" xmlns="http://www.w3.org/2000/svg">
  <!-- header band with roofline -->
  <rect class="band" x="0" y="0" width="1728" height="245"/>
  <polygon class="roof-gable" points="864,20 1310,248 418,248"/>
  <polygon class="roof-line" points="0,285 395,285 864,46 1330,285 1728,285 1728,310 1324,310 864,74 404,310 0,310"/>

  <!-- brand name -->
  <text class="brand-name" x="864" y="392" text-anchor="middle" textLength="440" lengthAdjust="spacingAndGlyphs">BRISKO</text>

  <!-- side accents -->
  <rect class="side-bar" x="0" y="415" width="30" height="385"/>
  <rect class="side-bar" x="1698" y="415" width="30" height="385"/>

  <!-- tagline -->
  <text class="tagline" x="48" y="598" textLength="1630" lengthAdjust="spacingAndGlyphs">UPGRADE YOUR ROOF</text>
  <text class="tagline" x="62" y="753" textLength="1606" lengthAdjust="spacingAndGlyphs">WITHOUT REPLACING IT</text>

  <!-- phone -->
  <g class="phone-icon">
    <circle class="phone-icon-ring" cx="205" cy="927" r="95"/>
    <rect class="phone-icon-body" x="174" y="870" width="62" height="116" rx="10"/>
    <rect class="phone-icon-detail" x="190" y="874" width="30" height="5" rx="2"/>
    <circle class="phone-icon-detail" cx="205" cy="974" r="5"/>
  </g>
  <text class="phone-number" x="325" y="995" textLength="1230" lengthAdjust="spacingAndGlyphs">(877) BRISKO-GO</text>

  <!-- license -->
  <text class="license" x="352" y="1103" textLength="1023" lengthAdjust="spacingAndGlyphs">RQMH LICENSE NUMBER: 4830516</text>

  <!-- footer band -->
  <rect class="band" x="0" y="1140" width="1728" height="156"/>
  <text class="website" x="95" y="1257" textLength="1505" lengthAdjust="spacingAndGlyphs">WWW.TRYVEXLO-DEMO.EXAMPLE</text>
</svg>
</body>
</html>
```